Creating a label for germicidal disposable wipes.

I need to create a label to put on our containers of germicidal disposable wipes. I am attaching an example of another germicidal wipe that I would like a similar format but more customized to look like my companies.

```html
<!DOCTYPE html>
<html lang="en">
<head>
<meta charset="utf-8">
<title>PURAMED Germicidal Wipes – Label</title>
<link href="https://fonts.googleapis.com/css2?family=Exo+2:ital,wght@0,400;0,500;0,600;0,700;0,800;1,800&family=Russo+One&family=Roboto+Mono:wght@400&display=swap" rel="stylesheet">
<style>
  :root{
    --navy:#27307f;
    --navy-deep:#1f2a85;
    --green:#34b34a;
    --green-mid:#2f9e5a;
    --teal:#1f7d7a;
    --red:#d52027;
    --ink:#1b1b1b;
    --page:#ffffff;
    --edge:#d5d8de;
  }
  *{box-sizing:border-box;margin:0;padding:0}
  html,body{width:800px;height:1200px;overflow:hidden;background:var(--page)}
  body{font-family:"Exo 2",sans-serif;color:var(--ink);position:relative}

  .label{
    position:absolute;left:20px;top:298px;width:760px;height:605px;
    border:1px solid var(--edge);border-radius:28px;overflow:hidden;background:#fff;
    box-shadow:0 2px 10px rgba(0,0,0,.08);
  }

  /* brand */
  .brand{position:absolute;left:38px;top:44px;display:flex;align-items:center;gap:10px}
  .brand-dot{width:34px;height:34px;border-radius:50%;background:var(--teal)}
  .brand-name{font-weight:700;font-size:21px;color:var(--navy);line-height:1}

  .product-name{
    position:absolute;left:36px;top:134px;font-family:"Russo One",sans-serif;
    font-size:80px;line-height:1;color:var(--navy-deep);letter-spacing:-1px;
  }
  .product-band{
    position:absolute;left:0;top:219px;width:420px;height:49px;
    background:linear-gradient(90deg,var(--navy) 0%,var(--navy) 70%,var(--green) 100%);
    clip-path:polygon(0 0,100% 0,96% 100%,0 100%);
  }
  .product-band span{
    position:absolute;left:38px;top:4px;font-weight:800;font-style:italic;
    font-size:35px;color:#fff;letter-spacing:1.5px;
  }

  /* claims */
  .claims{position:absolute;left:38px;top:288px;display:flex;gap:15px}
  .claim{
    width:54px;height:54px;border-radius:50%;border:3px solid var(--green);
    background:var(--teal);position:relative;overflow:hidden;
  }
  .claim::after{content:"";position:absolute;left:0;right:0;bottom:0;height:22px;background:#fff}
  .claim svg{position:absolute;left:50%;top:6px;transform:translateX(-50%)}
  .claim-text{
    position:absolute;left:0;right:0;bottom:3px;z-index:1;text-align:center;
    font-size:7px;font-weight:700;line-height:1;color:var(--navy);
  }

  .headline{position:absolute;left:38px;top:355px;font-weight:700;font-size:26px;color:var(--navy)}
  .headline em{font-style:normal;color:var(--green)}
  .chemical{position:absolute;left:38px;top:390px;font-weight:600;font-size:13px}

  .ingredients{position:absolute;left:38px;top:414px;width:386px}
  .ingredients-title{font-weight:600;font-size:13.5px;color:var(--green)}
  .ingredients-title small{font-family:"Roboto Mono",monospace;font-size:9.5px;color:var(--ink);font-weight:600;margin-left:4px}
  .ingredient{
    display:flex;font-family:"Roboto Mono",monospace;font-size:9.6px;line-height:12.6px;
  }
  .ingredient .name{white-space:nowrap;overflow:hidden;flex:1}
  .ingredient .name::after{content:" ...................................................................."}
  .ingredient .pct{padding-left:2px}

  /* bottom row */
  .warning{
    position:absolute;left:38px;top:534px;width:157px;height:33px;
    border:2px solid var(--red);border-radius:3px;
  }
  .warning svg{position:absolute;left:3px;top:8px}
  .warning .title{position:absolute;left:23px;top:2px;font-weight:800;font-size:13px;color:var(--red)}
  .warning .note{position:absolute;left:91px;top:3px;font-size:6px;line-height:6.5px}
  .warning .keep{position:absolute;left:23px;top:19px;font-weight:700;font-size:7.5px}

  .contains{position:absolute;left:217px;top:545px;font-weight:700;font-size:13px;color:var(--navy)}
  .divider{position:absolute;top:534px;width:1px;height:35px;background:var(--ink)}
  .count{position:absolute;left:281px;top:537px}
  .count b{display:block;font-weight:700;font-size:13.5px}
  .count span{font-size:9.5px}
  .traits{position:absolute;left:359px;top:535px;font-size:10px;line-height:12px}

  /* info panel */
  .info-panel{
    position:absolute;left:461px;top:0;width:299px;height:605px;
    border-top-left-radius:110px 150px;
    background:linear-gradient(160deg,var(--green) 0%,var(--green-mid) 14%,var(--teal) 35%,var(--navy-deep) 65%,var(--navy) 100%);
    color:#fff;
  }
  .info-block{position:absolute;left:19px;width:262px}
  .info-block h3{font-weight:600;font-size:13.5px;line-height:15px}
  .info-block p{font-size:10px;line-height:12.6px}
  .info-footer{position:absolute;left:19px;top:533px;display:flex;align-items:flex-start}
  .footer-mark{padding-right:10px;border-right:1px solid rgba(255,255,255,.7);height:34px}
  .footer-mark b{display:block;font-family:"Russo One",sans-serif;font-weight:400;font-size:18px;line-height:18px;color:#fff}
  .footer-mark i{font-weight:800;font-style:italic;font-size:9.5px;line-height:12px}
  .footer-info{padding-left:10px;font-size:9.5px;line-height:12px}
  .footer-info .co{color:var(--green)}
</style>
</head>
<body>
  <section class="label" aria-label="PURAMED Germicidal Wipes container label">
    <div class="brand">
      <span class="brand-dot"></span>
      <span class="brand-name">Kestrel Vital Solutions</span>
    </div>

    <h1 class="product-name">PURAMED</h1>
    <div class="product-band"><span>Germicidal Wipes</span></div>

    <div class="claims">
      <div class="claim">
        <svg width="18" height="18" viewBox="0 0 18 18"><circle cx="9" cy="10" r="6.5" fill="none" stroke="#fff" stroke-width="1.8"/><path d="M9 10V6.5M7 1.5h4" stroke="#fff" stroke-width="1.8" stroke-linecap="round"/></svg>
        <span class="claim-text">Disinfects in<br>2 Min</span>
      </div>
      <div class="claim">
        <svg width="20" height="18" viewBox="0 0 20 18"><path d="M3 16l4-12 4 6 3-4 4 10z" fill="#fff"/></svg>
        <span class="claim-text">Not a Skin or<br>Baby Wipe</span>
      </div>
      <div class="claim">
        <svg width="18" height="18" viewBox="0 0 18 18"><rect x="3" y="2" width="6" height="6" fill="#fff"/><path d="M3 9h12c0 4-3 6-6 6v2H6v-3c-2-1-3-3-3-5z" fill="#fff"/></svg>
        <span class="claim-text">Do not<br>Flush</span>
      </div>
    </div>

    <h2 class="headline">Surface <em>Disinfectant</em></h2>
    <p class="chemical">Alkyl C12-18 Dimethyl Ethyl Benzyl Ammonium Chloride</p>

    <div class="ingredients">
      <p class="ingredients-title">Active Ingredients: <small>Isopropyl Alcohol</small></p>
      <p class="ingredient"><span class="name">Lorem ipsum dolor sit amet, consectetuer adipiscing elit</span><span class="pct">0.25%</span></p>
      <p class="ingredient"><span class="name">Duis autem vel eum iriure dolor in hendrerit in vulputate velit</span><span class="pct">0.25%</span></p>
      <p class="ingredient"><span class="name">Ut wisi enim ad minim veniam, quis nostrud exerci</span><span class="pct">0.25%</span></p>
      <p class="ingredient"><span class="name">Lorem ipsum dolor sit amet, consectetuer adipiscing elit</span><span class="pct">0.25%</span></p>
      <p class="ingredient"><span class="name">Duis autem vel eum iriure dolor in hendrerit in vulputate velit</span><span class="pct">0.25%</span></p>
      <p class="ingredient"><span class="name">Ut wisi enim ad minim veniam, quis nostrud exerci</span><span class="pct">0.25%</span></p>
    </div>

    <div class="warning">
      <svg width="16" height="14" viewBox="0 0 16 14"><path d="M8 1l7 12H1z" fill="none" stroke="#d52027" stroke-width="1.6" stroke-linejoin="round"/><path d="M8 5v4M8 10.5v1" stroke="#d52027" stroke-width="1.6"/></svg>
      <span class="title">WARNING</span>
      <span class="note">See the Back Panel<br>for more details</span>
      <span class="keep">KEEP OUT OF REACH OF CHILDREN</span>
    </div>
    <span class="contains">Contains</span>
    <span class="divider" style="left:271px"></span>
    <div class="count"><b>160 Wipes</b><span>6 X 6-3/4 Inch</span></div>
    <span class="divider" style="left:350px"></span>
    <p class="traits">Disposable<br>Alcohol Scent<br>Non-Sterile</p>

    <aside class="info-panel">
      <div class="info-block" style="top:141px">
        <h3>Dummy Heading</h3>
        <p>Lorem ipsum dolor sit amet, consectetuer adipiscing elit, sed diam nonummy nibh euismod tincidunt ut laoreet dolore magna aliquam erat volutpat. Ut wisi enim ad minim veniam, quis nostrud exerci tation ullamcorper suscipit lobortis nisl ut aliquip ex ea commodo consequat.</p>
      </div>
      <div class="info-block" style="top:245px">
        <h3>Lorem Ipsum</h3>
        <p>Duis autem vel eum iriure dolor in hendrerit in vulputate velit esse molestie consequat, vel illum dolore eu feugiat nulla facilisis at vero eros et accumsan et iusto odio dignissim qui blandit praesent luptatum zzril delenit augue duis dolore te feugait nulla facilisi. Lorem ipsum dolor sit amet, cons ectetuer adipiscing elit, sed diam nonummy nibh</p>
      </div>
      <div class="info-block" style="top:362px">
        <h3>Dummy Heading</h3>
        <p>aliquam erat volutpat. Ut wisi enim ad minim veniam, quis nostrud exerci tation ullamcorper suscipit lobortis nisl ut aliquip ex ea commodo consequat.</p>
      </div>
      <div class="info-footer">
        <div class="footer-mark"><b>PURAMED</b><i>Germicidal Wipes</i></div>
        <div class="footer-info">KVS # KVW6678<br><span class="co">Kestrel Vital Solutions</span><br>United States</div>
      </div>
    </aside>
  </section>
</body>
</html>
```